Web Page Design (Coded). Winner can expect additional work to implement

My current employer (www.halvertonholdings.com.au) requires the establishment of a new web page (www.halvertonbluegrid.com.au) to promote safety and environmental products which will be sold to the oil / gas / mining and environmental sectors. The web page needs to be somehow aligned with the parent company page above (if only the colouring to appease my boss), yet innovate and awesome. The successful designer will be expected to provide coded files and be able to provide additional services to edit and launch the website. The website is currently operational but the content and format are both poor. The website will be predominantly based around promoting our products but will include a "buy online" section for some products which will be part of the website, but on a different tab / layer. Video's and flash will be part of the successful web page. Actually, I know very little about web pages so just go for gold and make it good and make it work. I am not adding any files at this point in time, but do post a message if you require any files.

Target Market(s)

Our products will be promoted to customers in Australia and SE Asia in the mining, oil and gas sectors predominantly with local government also a purchaser. Most purchase decisions will be made by males and people needing to solve problems quickly. They often won't care what product they receive as long as it does the job.

Industry/Entity Type

Safety

Requirements
Must have
• Must be aligned with our parent company page design (www.halvertonholdings.com.au). When I say aligned, I am talking effectively about fonts and colouring. The page design itself can be innovative beyond the parent company page design.
Somewhere on the page it must say we are a division of Halverton Holdings Pty Ltd.
Nice to have
• Easy to find products, read about them and download brochures. Links to be provided to "buy online" or "request a quote" next to each product, but without pricing.
It is essential that contacting us by phone, email etc... is easy to find through every layer of the page. This is essential. We would like some photo's on the home page scrolling through products, but these do not need to be large. Our current website (halvertonbluegrid.com.au) has photo's but they are too big.

```html
<!DOCTYPE html>
<html lang="en">
<head>
<meta charset="utf-8">
<title>Halverton Blue Grid</title>
<link href="https://fonts.googleapis.com/css2?family=Open+Sans:wght@400;600;700&display=swap" rel="stylesheet">
<style>
:root{
  --ink:#333;
  --muted:#777;
  --accent:#f2a51a;
  --brand:#1f3f8f;
  --red:#d0322a;
  --band:#2b2b2b;
  --footer:#2f2f2f;
  --footer-deep:#232323;
  --grey:#e9e9e9;
  --white:#fff;
}
*{box-sizing:border-box;margin:0;padding:0}
html,body{width:867px;height:1200px;overflow:hidden}
body{font-family:"Open Sans",Arial,sans-serif;color:var(--ink);background:var(--white);font-size:8px;line-height:1.5}
.wrap{width:668px;margin:0 auto;position:relative}

.site-header{height:70px;background:var(--white)}
.site-header .wrap{display:flex;justify-content:space-between;align-items:center;height:70px}
.brand{display:flex;align-items:center;gap:6px;font-weight:700;font-size:20px;color:var(--brand);letter-spacing:-.3px}
.brand-dot{width:12px;height:12px;border-radius:50%;background:var(--brand)}
.main-nav{display:flex;gap:0}
.main-nav a{display:block;padding:4px 15px;font-size:8px;font-weight:600;color:var(--ink);text-decoration:none}
.main-nav a.is-active{color:var(--accent);border-bottom:2px solid var(--accent)}

.hero{position:relative;height:232px;background:linear-gradient(180deg,#a9c2cf 0%,#5f7d4c 35%,#7e8b6d 60%,#b8ad93 100%)}
.hero-arrow{position:absolute;top:100px;width:18px;height:18px;border-radius:50%;background:rgba(0,0,0,.55)}
.hero-arrow svg{display:block}
.hero-arrow.prev{left:35px}.hero-arrow.next{right:35px}

.tagline-band{background:var(--band);height:78px;color:var(--white)}
.tagline-band .wrap{display:flex;justify-content:space-between;align-items:center;height:78px}
.tagline-band h1{font-size:19px;font-weight:400;letter-spacing:.2px;line-height:1.2}
.tagline-band p{font-size:9px;color:#ccc;margin-top:3px}
.btn-download{background:var(--accent);color:var(--white);font-weight:700;font-size:10px;padding:8px 12px;border-radius:2px}

.welcome{padding:20px 0 22px;text-align:center}
.section-title{font-size:11px;font-weight:700;color:var(--ink);letter-spacing:.2px}
.section-title::after{content:"";display:block;width:30px;height:2px;background:var(--accent);margin:5px auto 0}
.welcome p{margin-top:10px;font-size:7px;color:var(--muted);text-align:left;line-height:1.6}

.sectors{background:var(--grey);padding:20px 0 28px;height:178px}
.slider-dots{position:absolute;right:0;top:0;display:flex;gap:3px}
.slider-dots span{width:6px;height:6px;border-radius:50%;background:#aaa}
.sector-list{display:flex;justify-content:space-between;margin-top:16px}
.sector{width:205px;display:flex;gap:8px;align-items:flex-start;padding-top:6px}
.sector-icon{flex:none;width:40px;height:40px;border-radius:50%;background:radial-gradient(circle,#f3c23a 0 45%,#fff 46%);border:2px solid #ddd}
.sector h3{font-size:12px;font-weight:400;color:var(--ink)}
.sector p{font-size:6.5px;color:var(--muted);line-height:1.5;margin-top:2px}

.products{padding:24px 0 0;text-align:center;height:318px}
.product-list{display:flex;justify-content:space-between;margin-top:20px}
.product{width:205px}
.product-photo{height:120px}
.photo-data{background:linear-gradient(135deg,#c9d4de,#e7e3da 50%,#b46a4a)}
.photo-camera{background:linear-gradient(160deg,#6f8fa8,#d4a23a 55%,#3b3b3b)}
.photo-light{background:linear-gradient(170deg,#8fb0c9,#d9c06a 55%,#706a5a)}
.product h4{font-size:8px;font-weight:700;color:var(--brand);margin-top:8px}
.price{font-size:6.5px;color:var(--red);font-weight:600;margin-top:3px}

.site-footer{background:var(--footer);color:#ccc;height:172px}
.site-footer .wrap{display:flex;justify-content:space-between;padding-top:16px}
.footer-links{display:flex;gap:22px}
.footer-links ul{list-style:none}
.footer-links li{font-size:6.5px;line-height:2.1}
.newsletter{width:140px}
.newsletter h5,.contact-block h5{font-size:7.5px;font-weight:600;color:var(--white);margin-bottom:6px}
.field{height:14px;background:var(--white);margin-bottom:5px;font-size:6px;color:#999;padding:2px 4px}
.btn-signup{display:inline-block;background:#444;border:1px solid #777;color:var(--white);font-size:6.5px;padding:2px 7px}
.contact-block{width:130px;font-size:6.5px;line-height:1.8}
.social{display:flex;gap:4px;margin-top:8px}
.social span{width:12px;height:12px;border-radius:50%;background:#4a6fb0}
.copyright{background:var(--footer-deep);color:#999;font-size:6.5px;text-align:center;height:18px;line-height:18px}
</style>
</head>
<body>
<header class="site-header">
  <div class="wrap">
    <div class="brand"><span class="brand-dot"></span>Halverton Blue Grid</div>
    <nav class="main-nav">
      <a class="is-active" href="#">HOME</a><a href="#">ABOUT US</a><a href="#">PRODUCTS</a><a href="#">SOLUTION</a><a href="#">CONTACT US</a>
    </nav>
  </div>
</header>

<section class="hero" role="img" aria-label="Landscape photo of a river valley with green hills and a sandy shore">
  <span class="hero-arrow prev"><svg width="18" height="18"><path d="M10.5 5l-4 4 4 4" stroke="#fff" stroke-width="1.6" fill="none"/></svg></span>
  <span class="hero-arrow next"><svg width="18" height="18"><path d="M7.5 5l4 4-4 4" stroke="#fff" stroke-width="1.6" fill="none"/></svg></span>
</section>

<section class="tagline-band">
  <div class="wrap">
    <div>
      <h1>DISTRIBUTOR OF DISASTER MANT TECHNOGIES</h1>
      <p>Nemo enim ipsam voluptatem quia voluptas sit aut fugit, sed quia consequuntur</p>
    </div>
    <span class="btn-download">Download Brochures</span>
  </div>
</section>

<section class="welcome">
  <div class="wrap">
    <h2 class="section-title">WELCOME TO HALVERTON BLUE GRID</h2>
    <p>Halverton Blue Grid provides safety and environmental products, systems and services for the protection of people and property. Offering world leading technologies for remote monitoring, collection of data and control of public warning infrastructure, we are able to quickly improve situational awareness and help reduce risk. We are a division of Halverton Holdings Pty Ltd, serving mining, oil and gas and local government across the region.</p>
  </div>
</section>

<section class="sectors">
  <div class="wrap">
    <h2 class="section-title" style="text-align:center">MARKET SECTORS</h2>
    <div class="slider-dots"><span></span><span></span></div>
    <div class="sector-list">
      <div class="sector">
        <span class="sector-icon" role="img" aria-label="Solar panel icon"></span>
        <div><h3>Environmental</h3><p>Monitoring tools for water, air and weather that help teams act early, cut risk and protect the land around every site.</p></div>
      </div>
      <div class="sector">
        <span class="sector-icon" role="img" aria-label="Hard hat icon"></span>
        <div><h3>Mining</h3><p>Rugged warning and tracking systems built for pits and plants, keeping crews informed and safe in every shift.</p></div>
      </div>
      <div class="sector">
        <span class="sector-icon" role="img" aria-label="Oil barrel icon"></span>
        <div><h3>Oil and Gas</h3><p>Alert, lighting and camera solutions for remote fields and plants, ready to deploy fast where downtime costs.</p></div>
      </div>
    </div>
  </div>
</section>

<section class="products">
  <div class="wrap">
    <h2 class="section-title">PRODUCT CATEGORIES</h2>
    <div class="slider-dots" style="top:2px"><span></span><span></span></div>
    <div class="product-list">
      <div class="product">
        <div class="product-photo photo-data" role="img" aria-label="Photo of a worker with a data logging station"></div>
        <h4>Cloud Based Data Management</h4><p class="price">$ 89 ONLINE</p>
      </div>
      <div class="product">
        <div class="product-photo photo-camera" role="img" aria-label="Photo of a site worker in safety gear near CCTV equipment"></div>
        <h4>Remote Camera's and CCTV</h4><p class="price">$ 89 ONLINE</p>
      </div>
      <div class="product">
        <div class="product-photo photo-light" role="img" aria-label="Photo of a mobile lighting tower on site"></div>
        <h4>Lighting and Beacons</h4><p class="price">$ 89 ONLINE</p>
      </div>
    </div>
  </div>
</section>

<footer class="site-footer">
  <div class="wrap">
    <div class="footer-links">
      <ul><li>Home</li><li>About</li><li>News</li><li>Services</li><li>What We Do</li><li>Contact Us</li></ul>
      <ul><li>Oil &amp; Heating</li><li>Resources</li><li>Plan Now</li><li>Locations</li><li>Privacy Policy</li><li>Terms &amp; Conditions</li></ul>
      <ul><li>Resources</li><li>Plan Now</li><li>Locations</li><li>Privacy Policy</li><li>Terms &amp; Conditions</li></ul>
    </div>
    <div class="newsletter">
      <h5>NEWSLETTER SIGN UP</h5>
      <div class="field">Enter Name</div>
      <div class="field">Email Address</div>
      <span class="btn-signup">SIGN UP</span>
    </div>
    <div class="contact-block">
      <h5>Working Hours</h5>
      <p>Mon to Fri, 8am to 5pm local time<br>Sat by appointment only</p>
      <p>Phone: (000) 000 0000<br>Fax: (000) 000 0001</p>
      <div class="social"><span></span><span></span><span></span><span></span><span></span></div>
    </div>
  </div>
</footer>
<div class="copyright">© 2014 Halverton Blue Grid. All Rights Reserved</div>
</body>
</html>
```